New UI for electricity data tool

We are looking for a new UI for the website http://voltmeadow.net. Reassessing the structure of the website is as important as specific design choices. We have created a uniquely comprehensive set of global electricity generation data and now we are looking for creative solutions for how to make this data accessible. Researching and referencing other similar projects may be a good idea.

Goals:
• The website should clearly communicate the most important general conclusions that can be drawn from the data, including:
◦ The world as a whole is not moving away from fossil fuels for electricity generation
◦ There are substantial differences between regions
▪ Some regions have basically solved the problem – they already generate almost all of their electricity from non-fossil sources
▪ Some regions have greatly improved in terms of decarbonizing their electricity generation.
▪ Some regions have greatly deteriorated, in other words they are using a much higher share of fossil fuels to generate their electricity.
◦ There are substantial differences between energy sources. Regions that have successfully decarbonized their electricity generation have usually done so using hydro and/or nuclear. Other low-carbon energy sources have grown quickly in relative terms in the last few years but are so far contributing little in absolute numbers.
• The website should serve as inspiration for energy policy debates. The goal is to study the impact of existing policies around the world. Energy policy here refers to particular combinations of energy sources – ie how much have the countries invested in each type of electricity generation. The tool should help answer questions such as:
◦ Which countries have done the most in terms of decarbonizing their electricity generation?
◦ Which types of energy polices have lead to the fastest decarbonization processes around the world?
◦ If country A changed its energy policy to be more like country B, what would the likely impact be?

Challenges:
• There is a lot of data – it can be overwhelming to the user. It’s crucial to make the site easy to navigate. The main page should highlight the most important data, and it should also be straightforward to find more detailed data.
• Data availability varies from region to region. The current interface addresses this with the default option “Exclude regions with limited data”. We expect a better approach to dealing with this issue. For some regions and years energy sources are grouped together as for example “other renewables” whereas in other cases more detailed data is available.
• Credibility is crucial. Our data is based on a combination of data from KQ and the Tessaro Fund. It must be very clear throughout the site where each data set comes from.

Details:
• The current chart color schemes is loosely based on the carbon emissions from each energy source. This should not necessarily be so. The goal is to on the one hand communicate clearly the amounts of fossil vs non-fossil energy that are generated by each region. At the same time we also want to make it easy to view specific energy sources.

Inspirational websites:
• https://www.trendlooper.org/
• https://pelmarstatix.org/

Let's simplify. The main metric to focus on is Fernhollow Watt and the extent to which the world and each country has achieved it (eg Iceland 100%, France 88% and so on). I'm considering changing the name of the site to FernhollowWatt.org. We can use maps, charts and perhaps other tools to communicate this main message. What's the best way of doing this?

```html
<!DOCTYPE html>
<html lang="en">
<head>
<meta charset="utf-8">
<title>FernhollowWatt.org — Regions</title>
<link rel="stylesheet" href="https://fonts.googleapis.com/css2?family=Poppins:wght@300;400;500&display=swap">
<style>
  :root {
    --brand: #7553fb;
    --brand-deep: #6844ef;
    --page: #f7f7fb;
    --card: #ffffff;
    --ink: #23232b;
    --ink-soft: #55565f;
    --ink-muted: #7c7d86;
    --ink-faint: #b9bac4;
    --grid: #eeeff4;
    --hydro: #0b7fc1;
    --wind: #f39a1e;
    --fossil: #a3083a;
    --other: #8c8c8c;
    --range: #7db8ef;
    --range-knob: #3b8fe6;
    --shadow: 0 4px 18px rgba(60, 50, 120, 0.08);
  }
  * { box-sizing: border-box; margin: 0; padding: 0; }
  html, body { width: 1200px; height: 864px; overflow: hidden; }
  body {
    position: relative;
    background: var(--page);
    font-family: "Poppins", sans-serif;
    color: var(--ink);
  }

  /* ---------- Sidebar ---------- */
  .sidebar { position: absolute; left: 0; top: 0; width: 249px; height: 864px; }
  .sidebar__top {
    position: absolute; left: 0; top: 0; width: 249px; height: 173px;
    background: var(--brand); border-bottom-right-radius: 26px;
  }
  .sidebar__gutter {
    position: absolute; left: 0; top: 173px; width: 53px; height: 38px;
    background: var(--brand);
  }
  .sidebar__bottom {
    position: absolute; left: 0; top: 211px; width: 249px; height: 653px;
    background: var(--brand); border-top-right-radius: 26px;
  }
  .user-menu {
    position: absolute; left: 28px; top: 45px; width: 155px; height: 29px;
    border-radius: 15px; background: var(--brand-deep);
    display: flex; align-items: center; padding-left: 16px; gap: 10px;
    color: #fff; font-size: 11px; font-weight: 400; letter-spacing: 0.6px; white-space: nowrap;
  }
  .collapse-btn {
    position: absolute; left: 196px; top: 45px; width: 30px; height: 30px;
    border-radius: 50%; background: var(--brand-deep);
    display: flex; align-items: center; justify-content: center;
  }
  .nav { position: absolute; left: 0; top: 0; width: 249px; height: 864px; list-style: none; }
  .nav__item {
    position: absolute; left: 66px; height: 24px;
    display: flex; align-items: center; gap: 14px;
    color: #fff; font-size: 11.2px; font-weight: 400; letter-spacing: 0.7px; white-space: nowrap;
  }
  .nav__item svg { width: 18px; height: 18px; flex: none; }
  .nav__item--active {
    left: 53px; top: 173px; width: 196px; height: 38px;
    padding-left: 13px; background: var(--page);
    border-radius: 19px 0 0 19px; color: var(--brand);
  }

  /* ---------- Top bar ---------- */
  .filter {
    position: absolute; top: 45px; height: 30px; border-radius: 15px;
    background: var(--card); box-shadow: var(--shadow);
    display: flex; align-items: center; padding: 0 12px;
    font-size: 9.6px; font-weight: 300; color: var(--ink-muted); letter-spacing: 0.2px;
    white-space: nowrap;
  }
  .filter .chev { margin-left: auto; flex: none; }
  .filter--regions { left: 273px; width: 254px; padding-left: 11px; }
  .filter--regions .divider { width: 1px; height: 18px; background: #e8e8ee; margin: 0 8px 0 10px; }
  .filter--regions .placeholder { color: var(--ink-faint); font-size: 8px; }
  .filter--regions .search { margin-left: auto; }
  .filter--sort { left: 543px; width: 152px; }
  .filter--show { left: 709px; width: 72px; }
  .filter--exclude { left: 797px; width: 202px; }
  .bell { position: absolute; left: 1090px; top: 51px; }
  .avatar {
    position: absolute; left: 1112px; top: 45px; width: 29px; height: 29px;
    border-radius: 7px; background: linear-gradient(160deg, #6c5a4c, #2e2a2a);
  }
  .kebab { position: absolute; left: 1153px; top: 51px; }

  .source-chip {
    position: absolute; top: 95px; height: 30px; border-radius: 15px;
    background: var(--card); box-shadow: var(--shadow);
    display: flex; align-items: center; justify-content: center; gap: 6px;
    font-size: 8.6px; font-weight: 500; color: #1c2a4a; white-space: nowrap;
  }
  .source-chip--fund { left: 273px; width: 128px; }
  .source-chip--kq { left: 417px; width: 30px; border-radius: 50%; }
  .source-chip .mark { width: 14px; height: 14px; border-radius: 50%; background: #1c6fb3; }

  /* ---------- Region cards ---------- */
  .region { position: absolute; width: 430px; }
  .region__head {
    position: absolute; left: 0; top: 0;
    display: flex; align-items: baseline; white-space: nowrap;
  }
  .region__name {
    min-width: 88px; padding-right: 8px;
    font-size: 21px; font-weight: 500; letter-spacing: 0.6px; line-height: 28px;
  }
  .region__sort {
    font-size: 9.8px; font-weight: 300; color: var(--ink-muted); letter-spacing: 0.3px; line-height: 14px;
  }
  .region__summary {
    position: absolute; left: 20px; top: 35px; white-space: nowrap;
    font-size: 9.6px; font-weight: 300; color: var(--ink-soft); letter-spacing: 0.35px; line-height: 15.6px;
  }
  .chart-card {
    position: absolute; left: 1px; top: 78px; width: 424px; height: 202px;
    background: var(--card); border-radius: 11px; box-shadow: var(--shadow);
  }
  .chart-card svg { display: block; width: 424px; height: 202px; }

  .axis-label { font-size: 7px; fill: #9a9ba4; font-family: "Poppins", sans-serif; }
  .year { font-size: 6.4px; fill: #8d8e98; text-anchor: middle; font-family: "Poppins", sans-serif; }
  .year--focus { fill: var(--brand); }
  .grid { stroke: var(--grid); stroke-width: 1; fill: none; }
  .bars { fill: none; stroke-width: 11; }
  .bars--hydro { stroke: var(--hydro); }
  .bars--wind { stroke: var(--wind); }
  .bars--fossil { stroke: var(--fossil); }
  .bars--other { stroke: var(--other); }
  .pins { fill: none; stroke: none; }
  .pins--hydro { marker-start: url(#pin-hydro); marker-mid: url(#pin-hydro); marker-end: url(#pin-hydro); }
  .pins--wind { marker-start: url(#pin-wind); marker-mid: url(#pin-wind); marker-end: url(#pin-wind); }
  .pins--fossil { marker-start: url(#pin-fossil); marker-mid: url(#pin-fossil); marker-end: url(#pin-fossil); }
  .pins--other { marker-start: url(#pin-other); marker-mid: url(#pin-other); marker-end: url(#pin-other); }

  /* ---------- Pagination ---------- */
  .pager-btn {
    position: absolute; top: 786px; width: 83px; height: 26px; border-radius: 13px;
    background: var(--brand); color: #fff; font-size: 10px; font-weight: 400;
    display: flex; align-items: center; justify-content: center; gap: 8px;
  }
  .pager-btn--prev { left: 521px; }
  .pager-btn--next { left: 848px; }
  .page-num {
    position: absolute; top: 787px; width: 24px; height: 24px; margin-left: -12px;
    display: flex; align-items: center; justify-content: center;
    font-size: 9.6px; color: var(--ink); font-weight: 400;
  }
  .page-num--current { background: var(--brand); color: #fff; border-radius: 50%; }
</style>
</head>
<body>

<svg width="0" height="0" style="position:absolute" aria-hidden="true">
  <defs>
    <marker id="pin-hydro" viewBox="-6 -6 12 12" markerWidth="12" markerHeight="12" markerUnits="userSpaceOnUse"><circle r="4.3" fill="#fff" stroke="var(--hydro)" stroke-width="2.4"/></marker>
    <marker id="pin-wind" viewBox="-6 -6 12 12" markerWidth="12" markerHeight="12" markerUnits="userSpaceOnUse"><circle r="4.3" fill="#fff" stroke="var(--wind)" stroke-width="2.4"/></marker>
    <marker id="pin-fossil" viewBox="-6 -6 12 12" markerWidth="12" markerHeight="12" markerUnits="userSpaceOnUse"><circle r="4.3" fill="#fff" stroke="var(--fossil)" stroke-width="2.4"/></marker>
    <marker id="pin-other" viewBox="-6 -6 12 12" markerWidth="12" markerHeight="12" markerUnits="userSpaceOnUse"><circle r="4.3" fill="#fff" stroke="var(--other)" stroke-width="2.4"/></marker>
    <symbol id="chart-frame" viewBox="0 0 678 324">
      <path class="grid" d="M50 39H665M50 62H665M50 85H665M50 108H665M50 131H665M50 155H665M50 178H665M50 201H665M50 224H665M50 247H665M50 270H665"/>
      <g class="axis-label" text-anchor="end">
        <text x="42" y="42">100</text><text x="42" y="65">90</text><text x="42" y="88">80</text>
        <text x="42" y="111">70</text><text x="42" y="134">60</text><text x="42" y="157">50</text>
        <text x="42" y="181">40</text><text x="42" y="204">30</text><text x="42" y="227">20</text>
        <text x="42" y="250">10</text><text x="36" y="273">0</text>
      </g>
      <g>
        <text class="year" x="56" y="283">1971</text><text class="year" x="76" y="283">1972</text>
        <text class="year" x="96" y="283">1973</text><text class="year" x="116" y="283">1974</text>
        <text class="year" x="136" y="283">1975</text><text class="year" x="157" y="283">1976</text>
        <text class="year" x="177" y="283">1977</text><text class="year" x="197" y="283">1978</text>
        <text class="year" x="217" y="283">1979</text><text class="year" x="237" y="283">1980</text>
        <text class="year" x="257" y="283">1981</text><text class="year" x="277" y="283">1982</text>
        <text class="year year--focus" x="297" y="283">1983</text><text class="year" x="317" y="283">1984</text>
        <text class="year" x="337" y="283">1985</text><text class="year" x="358" y="283">1986</text>
        <text class="year" x="378" y="283">1987</text><text class="year" x="398" y="283">1988</text>
        <text class="year" x="418" y="283">1989</text><text class="year" x="438" y="283">1990</text>
        <text class="year" x="458" y="283">1991</text><text class="year" x="478" y="283">1992</text>
        <text class="year" x="498" y="283">1993</text><text class="year" x="518" y="283">1994</text>
        <text class="year" x="538" y="283">1995</text><text class="year" x="559" y="283">1996</text>
        <text class="year" x="579" y="283">1997</text><text class="year" x="599" y="283">1998</text>
        <text class="year" x="619" y="283">1999</text><text class="year" x="639" y="283">2000</text>
        <text class="year" x="659" y="283">2001</text>
      </g>
      <path d="M32 297l7 5-7 5z" fill="#4a4b55"/>
      <text class="year" x="57" y="305">1950</text>
      <path d="M70 302H640" stroke="#e6e8ef" stroke-width="3" stroke-linecap="round"/>
      <path d="M257 302H538" stroke="var(--range)" stroke-width="3"/>
      <circle cx="257" cy="302" r="5.5" fill="var(--range-knob)" stroke="#fff" stroke-width="2"/>
      <circle cx="538" cy="302" r="5.5" fill="var(--range-knob)" stroke="#fff" stroke-width="2"/>
      <text class="year" x="257" y="317">1971</text>
      <text class="year" x="538" y="317">2001</text>
      <text class="year" x="655" y="305">2020</text>
    </symbol>
  </defs>
</svg>

<!-- Sidebar -->
<aside class="sidebar">
  <div class="sidebar__top"></div>
  <div class="sidebar__gutter"></div>
  <div class="sidebar__bottom"></div>

  <div class="user-menu">MARLON T OKAFOR
    <svg width="9" height="6" viewBox="0 0 9 6"><path d="M1 1l3.5 3.5L8 1" fill="none" stroke="#fff" stroke-width="1.2"/></svg>
  </div>
  <div class="collapse-btn">
    <svg width="8" height="10" viewBox="0 0 8 10"><path d="M6 1L2 5l4 4" fill="none" stroke="#fff" stroke-width="1.2"/></svg>
  </div>

  <ul class="nav">
    <li class="nav__item nav__item--active">
      <svg viewBox="0 0 18 18" fill="none" stroke="currentColor" stroke-width="1.2"><circle cx="9" cy="9" r="7"/><path d="M2 9h14M9 2c3 3 3 11 0 14M9 2c-3 3-3 11 0 14"/></svg>
      REGIONS
    </li>
    <li class="nav__item" style="top:241px">
      <svg viewBox="0 0 18 18" fill="none" stroke="currentColor" stroke-width="1.2"><circle cx="9" cy="9" r="7.5"/><path d="M9 4.5c2 2.6 3 4.2 3 5.6a3 3 0 0 1-6 0c0-1.4 1-3 3-5.6z"/></svg>
      ENERGY SOURCES
    </li>
    <li class="nav__item" style="top:301px">
      <svg viewBox="0 0 18 18" fill="none" stroke="currentColor" stroke-width="1.2"><path d="M7 2l8 3v8l-8-3z"/><path d="M4 5l8 3v8l-8-3z"/><circle cx="4" cy="14" r="2.5"/></svg>
      CHANGES
    </li>
    <li class="nav__item" style="top:361px">
      <svg viewBox="0 0 18 18" fill="none" stroke="currentColor" stroke-width="1.2"><ellipse cx="9" cy="4" rx="7" ry="2.5"/><path d="M2 4v10c0 1.4 3.1 2.5 7 2.5s7-1.1 7-2.5V4M2 7.3c0 1.4 3.1 2.5 7 2.5s7-1.1 7-2.5M2 10.6c0 1.4 3.1 2.5 7 2.5s7-1.1 7-2.5"/></svg>
      DATA SOURCES
    </li>
    <li class="nav__item" style="top:545px">
      <svg viewBox="0 0 18 18" fill="none" stroke="currentColor" stroke-width="1.2"><circle cx="9" cy="9" r="2.8"/><path d="M7.6 1.5h2.8l.4 2 1.6.9 1.9-.7 1.4 2.4-1.5 1.4v1.9l1.5 1.4-1.4 2.4-1.9-.7-1.6.9-.4 2H7.6l-.4-2-1.6-.9-1.9.7-1.4-2.4 1.5-1.4V7.5L2.3 6.1l1.4-2.4 1.9.7 1.6-.9z"/></svg>
      SETTINGS
    </li>
    <li class="nav__item" style="top:591px">
      <svg viewBox="0 0 18 18" fill="none" stroke="currentColor" stroke-width="1.2"><path d="M10 2H3v14h7M7 9h9M13 6l3 3-3 3"/></svg>
      LOGOUT
    </li>
  </ul>
</aside>

<!-- Top bar -->
<div class="filter filter--regions">Selected Regions
  <svg width="8" height="5" viewBox="0 0 8 5" style="margin-left:8px"><path d="M1 1l3 3 3-3" fill="none" stroke="#999" stroke-width="1"/></svg>
  <span class="divider"></span>
  <span class="placeholder">Type here</span>
  <svg class="search" width="11" height="11" viewBox="0 0 11 11"><circle cx="4.6" cy="4.6" r="3.8" fill="none" stroke="#888" stroke-width="1.1"/><path d="M7.4 7.4L10.4 10.4" stroke="#888" stroke-width="1.1"/></svg>
</div>
<div class="filter filter--sort">Sort by low-carbon (%)
  <svg class="chev" width="8" height="5" viewBox="0 0 8 5"><path d="M1 1l3 3 3-3" fill="none" stroke="#999" stroke-width="1"/></svg>
</div>
<div class="filter filter--show">Show %
  <svg class="chev" width="8" height="5" viewBox="0 0 8 5"><path d="M1 1l3 3 3-3" fill="none" stroke="#999" stroke-width="1"/></svg>
</div>
<div class="filter filter--exclude">Exclude regions with limited data
  <svg class="chev" width="8" height="5" viewBox="0 0 8 5"><path d="M1 1l3 3 3-3" fill="none" stroke="#999" stroke-width="1"/></svg>
</div>

<svg class="bell" width="18" height="20" viewBox="0 0 18 20" fill="none" stroke="#8a8b95" stroke-width="1.1">
  <path d="M4 14V9a5 5 0 0 1 10 0v5l1.5 1.5h-13z"/><path d="M7.5 17.5a1.6 1.6 0 0 0 3 0"/>
  <circle cx="14.5" cy="3.5" r="2.6" fill="var(--brand)" stroke="none"/>
</svg>
<div class="avatar" role="img" aria-label="Profile photo of the signed-in user"></div>
<svg class="kebab" width="6" height="16" viewBox="0 0 6 16"><circle cx="3" cy="2" r="1.5" fill="#7c7d86"/><circle cx="3" cy="8" r="1.5" fill="#7c7d86"/><circle cx="3" cy="14" r="1.5" fill="#7c7d86"/></svg>

<div class="source-chip source-chip--fund"><span class="mark"></span>Tessaro Fund</div>
<div class="source-chip source-chip--kq">KQ</div>

<!-- Spain -->
<section class="region" style="left:277px;top:142px">
  <div class="region__head"><h2 class="region__name">Spain</h2><p class="region__sort">Sort by low-carbon (%)</p></div>
  <p class="region__summary">53% of the electricity in Spain is generated from low-carbon power.<br>The primary low-carbon power source is nuclear.</p>
  <div class="chart-card">
    <svg viewBox="0 0 678 324" role="img" aria-label="Low-carbon share of electricity in Spain, 1971 to 2001">
      <use href="#chart-frame" width="678" height="324"/>
      <path class="bars bars--hydro" d="M56 256V136M96 256V143M136 256V125M157 256V108M177 256V104M197 256V94M237 256V94M378 256V120M398 256V125M418 256V129M458 256V115M518 256V106M559 256V81M579 256V81M599 256V76M639 256V134M659 256V134"/>
      <path class="bars bars--wind" d="M76 256V120M257 256V85M317 256V178M498 256V101M619 256V62"/>
      <path class="bars bars--fossil" d="M116 256V113M217 256V99M297 256V175M438 256V104M478 256V97M538 256V85"/>
      <path class="bars bars--other" d="M277 256V159M337 256V173M358 256V155"/>
      <path class="pins pins--hydro" d="M56 136 96 143 136 125 157 108 177 104 197 94 237 94 378 120 398 125 418 129 458 115 518 106 559 81 579 81 599 76 639 134 659 134"/>
      <path class="pins pins--wind" d="M76 120 257 85 317 178 498 101 619 62"/>
      <path class="pins pins--fossil" d="M116 113 217 99 297 175 438 104 478 97 538 85"/>
      <path class="pins pins--other" d="M277 159 337 173 358 155"/>
    </svg>
  </div>
</section>

<!-- France -->
<section class="region" style="left:736px;top:142px">
  <div class="region__head"><h2 class="region__name">France</h2><p class="region__sort">Sort by low-carbon (%)</p></div>
  <p class="region__summary">53% of the electricity in Spain is generated from low-carbon power.<br>The primary low-carbon power source is nuclear.</p>
  <div class="chart-card">
    <svg viewBox="0 0 678 324" role="img" aria-label="Low-carbon share of electricity in France, 1971 to 2001">
      <use href="#chart-frame" width="678" height="324"/>
      <path class="bars bars--hydro" d="M56 256V131M76 256V131M116 256V78M136 256V81M157 256V81M197 256V106M297 256V136M317 256V134M337 256V131M478 256V97M518 256V97M538 256V106M559 256V111M579 256V129M619 256V150M659 256V134"/>
      <path class="bars bars--wind" d="M96 256V62M217 256V101M257 256V62M398 256V178M458 256V85M639 256V120"/>
      <path class="bars bars--fossil" d="M177 256V85M237 256V94M277 256V106M418 256V178M498 256V101M599 256V115"/>
      <path class="bars bars--other" d="M358 256V152M378 256V173M438 256V161"/>
      <path class="pins pins--hydro" d="M56 131 76 131 116 78 136 81 157 81 197 106 297 136 317 134 337 131 478 97 518 97 538 106 559 111 579 129 619 150 659 134"/>
      <path class="pins pins--wind" d="M96 62 217 101 257 62 398 178 458 85 639 120"/>
      <path class="pins pins--fossil" d="M177 85 237 94 277 106 418 178 498 101 599 115"/>
      <path class="pins pins--other" d="M358 152 378 173 438 161"/>
    </svg>
  </div>
</section>

<!-- Italy -->
<section class="region" style="left:277px;top:456px">
  <div class="region__head"><h2 class="region__name">Italy</h2><p class="region__sort">Sort by low-carbon (%)</p></div>
  <p class="region__summary">53% of the electricity in Spain is generated from low-carbon power.<br>The primary low-carbon power source is nuclear.</p>
  <div class="chart-card">
    <svg viewBox="0 0 678 324" role="img" aria-label="Low-carbon share of electricity in Italy, 1971 to 2001">
      <use href="#chart-frame" width="678" height="324"/>
      <path class="bars bars--hydro" d="M96 256V159M157 256V127M197 256V108M237 256V108M297 256V129M358 256V108M398 256V141M418 256V148M458 256V129M478 256V143M518 256V120M579 256V92M599 256V88M659 256V150"/>
      <path class="bars bars--wind" d="M56 256V182M76 256V131M257 256V101M498 256V115"/>
      <path class="bars bars--fossil" d="M116 256V131M217 256V113M317 256V113M378 256V108M438 256V120M538 256V101M559 256V120M619 256V120"/>
      <path class="bars bars--other" d="M136 256V175M177 256V166M277 256V166M337 256V175M639 256V175"/>
      <path class="pins pins--hydro" d="M96 159 157 127 197 108 237 108 297 129 358 108 398 141 418 148 458 129 478 143 518 120 579 92 599 88 659 150"/>
      <path class="pins pins--wind" d="M56 182 76 131 257 101 498 115"/>
      <path class="pins pins--fossil" d="M116 131 217 113 317 113 378 108 438 120 538 101 559 120 619 120"/>
      <path class="pins pins--other" d="M136 175 177 166 277 166 337 175 639 175"/>
    </svg>
  </div>
</section>

<!-- Sweden -->
<section class="region" style="left:736px;top:456px">
  <div class="region__head"><h2 class="region__name">Sweden</h2><p class="region__sort">Sort by low-carbon (%)</p></div>
  <p class="region__summary">53% of the electricity in Spain is generated from low-carbon power.<br>The primary low-carbon power source is nuclear.</p>
  <div class="chart-card">
    <svg viewBox="0 0 678 324" role="img" aria-label="Low-carbon share of electricity in Sweden, 1971 to 2001">
      <use href="#chart-frame" width="678" height="324"/>
      <path class="bars bars--hydro" d="M56 256V152M96 256V159M136 256V143M177 256V122M237 256V113M337 256V150M378 256V138M418 256V143M458 256V129M498 256V122M518 256V106M559 256V99M599 256V94M659 256V150"/>
      <path class="bars bars--wind" d="M76 256V136M257 256V104M317 256V180M619 256V78"/>
      <path class="bars bars--fossil" d="M116 256V131M157 256V166M197 256V113M217 256V118M297 256V180M438 256V122M478 256V113M538 256V104M579 256V178M639 256V99"/>
      <path class="bars bars--other" d="M277 256V166M358 256V155M398 256V175"/>
      <path class="pins pins--hydro" d="M56 152 96 159 136 143 177 122 237 113 337 150 378 138 418 143 458 129 498 122 518 106 559 99 599 94 659 150"/>
      <path class="pins pins--wind" d="M76 136 257 104 317 180 619 78"/>
      <path class="pins pins--fossil" d="M116 131 157 166 197 113 217 118 297 180 438 122 478 113 538 104 579 178 639 99"/>
      <path class="pins pins--other" d="M277 166 358 155 398 175"/>
    </svg>
  </div>
</section>

<!-- Pagination -->
<nav aria-label="Pages">
  <div class="pager-btn pager-btn--prev">
    <svg width="12" height="8" viewBox="0 0 12 8"><path d="M11 4H1M4 1L1 4l3 3" fill="none" stroke="#fff" stroke-width="1.1"/></svg>Prev
  </div>
  <span class="page-num" style="left:622px">1</span>
  <span class="page-num" style="left:643px">2</span>
  <span class="page-num page-num--current" style="left:666px">3</span>
  <span class="page-num" style="left:688px">4</span>
  <span class="page-num" style="left:711px">5</span>
  <span class="page-num" style="left:733px">6</span>
  <span class="page-num" style="left:756px">7</span>
  <span class="page-num" style="left:778px">8</span>
  <span class="page-num" style="left:801px">…</span>
  <span class="page-num" style="left:826px">20</span>
  <div class="pager-btn pager-btn--next">Next
    <svg width="12" height="8" viewBox="0 0 12 8"><path d="M1 4h10M8 1l3 3-3 3" fill="none" stroke="#fff" stroke-width="1.1"/></svg>
  </div>
</nav>

</body>
</html>
```